Our winery needs a company flyer

We need a flyer describing our family winery and our excellent wines. We would like to be attractive fresh and young for people from 30 to 50 years old. the vineyards are planted from the family and our wines are a selected production. We love nature !
The final design should communicate "a good job produce a good wine". look at our website www.belstradivini.ch

```html
<!DOCTYPE html>
<html lang="en">
<head>
<meta charset="utf-8">
<title>Belstradi Wines – Flyer</title>
<link rel="stylesheet" href="https://fonts.googleapis.com/css2?family=Abril+Fatface&family=Alike&family=Arimo:wght@700&display=swap">
<style>
  :root {
    --teal: #1f7d78;
    --teal-deep: #176661;
    --teal-light: #5fd6c4;
    --band: #2a9a8c;
    --cream: #f3eee3;
    --ink: #1d1d1d;
    --stage: #5b5b5b;
  }
  html, body {
    margin: 0;
    width: 1200px;
    height: 1058px;
    overflow: hidden;
    background: var(--stage);
  }
  .flyer {
    position: absolute;
    left: 246px;
    top: 29px;
    width: 707px;
    height: 1000px;
    background: var(--cream);
    overflow: hidden;
    box-shadow: 0 6px 18px rgba(0,0,0,.35);
  }
  .flyer__top {
    position: absolute;
    left: 0; top: 0;
    width: 707px;
    height: 520px;
    background: linear-gradient(180deg, var(--teal) 0%, var(--teal-deep) 100%);
  }
  .notch {
    position: absolute;
    left: 50%;
    transform: translateX(-50%);
    width: 130px;
    height: 60px;
  }
  .notch--top {
    top: 0;
    background: var(--cream);
    border-radius: 0 0 65px 65px;
  }
  .notch--bottom {
    bottom: 0;
    background: var(--teal);
    border-radius: 65px 65px 0 0;
  }
  .brand {
    position: absolute;
    top: 68px;
    width: 100%;
    text-align: center;
    font-family: "Alike", serif;
    font-size: 46px;
    line-height: 1;
    letter-spacing: 2px;
    color: var(--teal-light);
    margin: 0;
  }
  .headline {
    position: absolute;
    top: 126px;
    width: 100%;
    text-align: center;
    font-family: "Abril Fatface", serif;
    font-size: 64px;
    line-height: 1;
    color: var(--cream);
    margin: 0;
  }
  .subtitle {
    position: absolute;
    top: 210px;
    width: 100%;
    text-align: center;
    font-family: "Alike", serif;
    font-size: 30px;
    line-height: 1.12;
    color: var(--teal-light);
    margin: 0;
  }
  .photo {
    position: absolute;
    top: 372px;
    height: 150px;
  }
  .photo--grower {
    left: 0;
    width: 230px;
    background: linear-gradient(135deg, #b89a64 0%, #6b8a4e 55%, #2f8a4a 100%);
  }
  .photo--wall {
    right: 0;
    width: 200px;
    background: linear-gradient(135deg, #8c8f94 0%, #6f7378 60%, #9a8c6e 100%);
  }
  .torn-edge {
    position: absolute;
    left: 0;
    top: 505px;
    width: 707px;
    height: 30px;
  }
  .bottles {
    position: absolute;
    left: 200px;
    top: 300px;
    width: 320px;
    height: 300px;
    background: linear-gradient(180deg, #2a2a2a 0%, #111 45%, #f4f1ea 45%, #f4f1ea 78%, #111 78%, #1a1a1a 100%);
    border-radius: 14px 14px 8px 8px;
  }
  .bottles__reflection {
    position: absolute;
    left: 200px;
    top: 602px;
    width: 320px;
    height: 36px;
    background: linear-gradient(180deg, rgba(0,0,0,.12), rgba(0,0,0,0));
  }
  .tagline {
    position: absolute;
    margin: 0;
    font-family: "Alike", serif;
    color: #ffffff;
    background: var(--band);
    font-size: 23px;
    line-height: 1.2;
    padding: 5px 16px 6px;
    white-space: nowrap;
  }
  .tagline--first { left: 80px; top: 648px; }
  .tagline--second { left: 150px; top: 696px; background: var(--teal-deep); }
  .contact-call {
    position: absolute;
    top: 756px;
    width: 100%;
    text-align: center;
    font-family: "Abril Fatface", serif;
    font-size: 28px;
    line-height: 1.1;
    color: var(--ink);
    margin: 0;
  }
  .divider {
    position: absolute;
    left: 140px;
    top: 804px;
    width: 430px;
    height: 12px;
  }
  .phone {
    position: absolute;
    top: 824px;
    width: 100%;
    text-align: center;
    font-family: "Arimo", sans-serif;
    font-weight: 700;
    font-size: 38px;
    line-height: 46px;
    color: var(--teal);
  }
  .email {
    position: absolute;
    top: 882px;
    width: 100%;
    text-align: center;
    font-family: "Alike", serif;
    font-size: 23px;
    line-height: 30px;
    color: var(--teal);
  }
  .icon {
    display: inline-block;
    vertical-align: middle;
    margin-right: 12px;
  }
</style>
</head>
<body>
  <main class="flyer">
    <section class="flyer__top">
      <div class="notch notch--top"></div>
      <p class="brand">BELSTRADI</p>
      <h1 class="headline">We Love Nature!</h1>
      <p class="subtitle">Experience the Finest<br>Wine Tasting</p>
      <div class="photo photo--grower" role="img" aria-label="Photo of a young vine grower in a straw hat beside crates of harvested grapes"></div>
      <div class="photo photo--wall" role="img" aria-label="Photo of a man walking beside an old stone wall in the vineyard"></div>
    </section>

    <svg class="torn-edge" viewBox="0 0 707 30" preserveAspectRatio="none" aria-hidden="true">
      <path d="M0 0 H707 V8 L680 14 L650 6 L620 16 L590 9 L560 18 L520 10 L480 20 L440 12 L400 22 L360 13 L320 20 L280 10 L240 18 L200 9 L160 17 L120 8 L80 16 L40 7 L0 14 Z" fill="var(--teal-deep)"/>
    </svg>

    <div class="bottles" role="img" aria-label="Photo of four bottles of Ticino Merlot red wine standing in a row"></div>
    <div class="bottles__reflection" aria-hidden="true"></div>

    <p class="tagline tagline--first">The vineyards are planted from the family and</p>
    <p class="tagline tagline--second">our wines are a selected production.</p>

    <p class="contact-call">Contact us for tasting our excellent wines</p>

    <svg class="divider" viewBox="0 0 430 12" aria-hidden="true">
      <line x1="0" y1="6" x2="430" y2="6" stroke="var(--teal)" stroke-width="2"/>
      <circle cx="215" cy="6" r="5" fill="var(--teal)"/>
    </svg>

    <div class="phone">
      <svg class="icon" width="24" height="40" viewBox="0 0 24 40" aria-hidden="true">
        <rect x="2" y="2" width="20" height="36" rx="4" fill="none" stroke="var(--ink)" stroke-width="3"/>
        <line x1="8" y1="32" x2="16" y2="32" stroke="var(--ink)" stroke-width="2.5"/>
      </svg>+41 91 5550174
    </div>

    <div class="email">
      <svg class="icon" width="30" height="20" viewBox="0 0 30 20" aria-hidden="true">
        <rect x="1" y="1" width="28" height="18" fill="var(--ink)"/>
        <polyline points="1,1 15,11 29,1" fill="none" stroke="var(--cream)" stroke-width="2"/>
      </svg>info@belstradivini.ch
    </div>

    <div class="notch notch--bottom"></div>
  </main>
</body>
</html>
```